Business Card Design Project

I need a business card designed from scratch. I have an existing logo that I can upload in Illustrator for modification or redesign.

The Company is called Rank Harbor http://rankharbor.com.au and we provide Search Engine Optimization services to Australian businesses. The current logo signifies an increase in visitors, profits etc...

There are no restrictions as to the redesign - colours, style etc are all open to change.

Cards will be full colour and one sided printed at http://www.printlorvex.com.au so check their requirements for file format and sizes etc.

I will expect all original files upon completion of project.

Target Market(s)

Any business with a web site looking to improve their search engine rankings

Industry/Entity Type

Business

Requirements
Must have
• I like modern, sleek designs. Clean, not fussy, uncluttered.

```html
<!DOCTYPE html>
<html lang="en">
<head>
<meta charset="utf-8">
<title>Rank Harbor – Business Card</title>
<link rel="stylesheet" href="https://fonts.googleapis.com/css2?family=Open+Sans:wght@400;700;800&display=swap">
<style>
  :root {
    --page-bg: #ecebe8;
    --card-blue-light: #6fb0e0;
    --card-blue: #3b82c4;
    --card-blue-dark: #2762a8;
    --band-white: #ffffff;
    --brand-navy: #2f5fa3;
    --brand-yellow: #f2c531;
    --text-white: #ffffff;
    --text-soft: #e3eefa;
  }
  * { margin: 0; padding: 0; box-sizing: border-box; }
  html, body {
    width: 1200px; height: 1023px; overflow: hidden;
    background: var(--page-bg);
    font-family: "Open Sans", Arial, sans-serif;
  }
  .canvas {
    position: relative; width: 1200px; height: 1023px;
    display: flex; align-items: center; justify-content: center;
  }
  .business-card {
    position: relative; width: 900px; height: 550px;
    background: radial-gradient(ellipse at 62% 38%, var(--card-blue-light) 0%, var(--card-blue) 45%, var(--card-blue-dark) 100%);
    box-shadow: 0 10px 30px rgba(0,0,0,0.18);
    overflow: hidden;
  }
  .logo-band {
    position: absolute; left: 0; top: 262px;
    width: 410px; height: 150px;
    background: var(--band-white);
    display: flex; align-items: center; justify-content: center; gap: 18px;
  }
  .logo-mark { width: 34px; height: 34px; border-radius: 50%; background: var(--brand-yellow); }
  .logo-name {
    font-weight: 800; font-size: 44px; line-height: 1;
    color: var(--brand-navy); text-transform: uppercase; letter-spacing: 1px;
  }
  .contact-block {
    position: absolute; left: 440px; top: 170px;
    color: var(--text-white);
  }
  .person-name { font-size: 19px; font-weight: 400; color: var(--text-soft); }
  .person-title { font-size: 19px; font-weight: 700; margin-top: 4px; }
  .contact-list { list-style: none; margin-top: 52px; font-size: 19px; line-height: 1.5; }
  .contact-list .label { font-weight: 700; }
</style>
</head>
<body>
  <main class="canvas">
    <section class="business-card" aria-label="Rank Harbor business card">
      <div class="logo-band">
        <span class="logo-mark" aria-hidden="true"></span>
        <span class="logo-name">Rank Harbor</span>
      </div>
      <div class="contact-block">
        <p class="person-name">Neil Carver</p>
        <p class="person-title">Internet Marketing Consultant</p>
        <ul class="contact-list">
          <li><span class="label">Tel No.</span> : 1300 482915</li>
          <li><span class="label">Email</span> : neil@rankharbor.com.au</li>
          <li><span class="label">Website</span>: www.rankharbor.com.au</li>
        </ul>
      </div>
    </section>
  </main>
</body>
</html>
```